Verpackungen für Tee
Zielgruppe
Liebe Kreative,
UMREL spricht Frauen im Alter von ca. 30 - 45 Jahren an. Im Teebereich kann sich diese Gruppe aber auch öffnen, gegen oben und unten.
Die Frau, die meinen Tee kauft, legt Wert auf einen gesunden und aktiven Lifestyle (hoffentlich ;))!
Aufgabenstellung
Die bereits bestehende Supplemente Linie strahlt in einem frischen Ice Blue,
Den neuen Tee (soon Teesortiment) stelle ich mir eher mit Erdtönen oder allenfalls in einem schönen Oliv vor.
Das Packing clean sein, gesund (aber nicht zu alternativ) und einfach Lust machen, ihn zu trinken.
Vertrauen sollte vermittelt werden.
Das UMREL Herz zentral in der Mitte fände ich sehr schön. Jedoch bin ich auf offen, für eine neue Idee.
Die genauen Abmessungen des Teekartons finden Sie in den Uploads.
NAME DES PRODUKTES: Kelso Drift

```html
<!DOCTYPE html>
<html lang="de">
<head>
<meta charset="utf-8">
<title>Kelso Drift – Teeverpackung</title>
<link rel="stylesheet" href="https://fonts.googleapis.com/css2?family=Antonio:wght@200&family=Josefin+Sans:wght@300&display=swap">
<style>
  :root {
    --backdrop: #ecebe6;
    --paper: #f7f7f2;
    --olive-light: #d9e2b8;
    --olive-mid: #b4c776;
    --olive-deep: #92ad3a;
    --ink: #2b2b2b;
    --brand-grey: #3a3a3c;
  }
  * { margin: 0; padding: 0; box-sizing: border-box; }
  html, body {
    width: 1200px;
    height: 1200px;
    overflow: hidden;
    background: var(--backdrop);
  }
  .canvas {
    width: 1200px;
    height: 1200px;
    display: flex;
    align-items: center;
    justify-content: center;
  }
  .pack-front {
    position: relative;
    width: 880px;
    height: 880px;
    background: var(--paper);
    overflow: hidden;
  }
  .watercolor-field {
    position: absolute;
    inset: 0;
    background:
      radial-gradient(ellipse 42% 38% at 58% 48%, var(--olive-deep) 0%, rgba(146,173,58,0.55) 45%, rgba(146,173,58,0) 75%),
      radial-gradient(ellipse 40% 45% at 25% 40%, var(--olive-mid) 0%, rgba(180,199,118,0.4) 50%, rgba(180,199,118,0) 80%),
      radial-gradient(ellipse 60% 30% at 40% 8%, var(--olive-light) 0%, rgba(217,226,184,0) 80%),
      linear-gradient(135deg, #e4ead0 0%, var(--paper) 70%);
  }
  .product-label {
    position: absolute;
    right: 96px;
    bottom: 200px;
    font-family: "Antonio", "Arial Narrow", sans-serif;
    font-weight: 200;
    font-size: 64px;
    line-height: 1.08;
    letter-spacing: 0.22em;
    color: var(--ink);
    text-transform: uppercase;
  }
  .brand-name {
    position: absolute;
    right: 70px;
    bottom: 90px;
    display: flex;
    align-items: center;
    gap: 18px;
    font-family: "Josefin Sans", "Helvetica", sans-serif;
    font-weight: 300;
    font-size: 86px;
    letter-spacing: 0.02em;
    color: var(--brand-grey);
  }
  .brand-dot {
    width: 34px;
    height: 34px;
    border-radius: 50%;
    background: #e03a2f;
  }
</style>
</head>
<body>
  <main class="canvas">
    <section class="pack-front">
      <div class="watercolor-field" role="img" aria-label="Olivgrüne Aquarell-Pinselflächen auf hellem Grund"></div>
      <h1 class="product-label">Kelso<br>Drift</h1>
      <div class="brand-name"><span class="brand-dot"></span>UMREL</div>
    </section>
  </main>
</body>
</html>
```